TRV Mechanical Solutions Business Card Design

Business card design

Thinking just large logo on one side with a phone number and the back side is contact info with services we offer with a industrial plant across the bottom of the card

See must haves. I will be laser etching these business cards on black metal business cards as well as full color card stock. So must be bold and professional.

Target Market(s)

Industrial manufacturing

Contact Information for Business Card

Industrial manufacturing construction business specializing in consulting project managment and completing projects turn key

Font styles to use
Other font styles liked:
• See Logo for colors and font style

Requirements
Must have
• TRV Mechanical Solutions
• Gerald Munroe
• 2847 Alderwick Lane
• Bel Air, MD, 21047
• Project Managment
• Consulting
• Turn Key Industrial Projects
• I’d like a industrial manufacturing “cityline” on the back side bottom of the
• I’d like to be able to print these business cards in regular color on card stock but I’d also like the design to be etched into black metal business cards

```html
<!DOCTYPE html>
<html lang="en">
<head>
<meta charset="utf-8">
<title>TRV Mechanical Solutions — Business Card</title>
<link rel="stylesheet" href="https://fonts.googleapis.com/css2?family=Rajdhani:wght@600&family=Orbitron:wght@400&family=Oswald:wght@300&family=Roboto:wght@400&display=swap">
<style>
  :root {
    --backdrop: #7f847c;
    --card-black: #1e1e1e;
    --panel-light: #dadada;
    --gold: #8c6a05;
    --gold-deep: #5e4703;
    --slate: #565454;
    --text-grey: #bdbdbd;
    --text-white: #f2f2f2;
  }
  * { margin: 0; padding: 0; box-sizing: border-box; }
  html, body {
    width: 1200px; height: 900px; overflow: hidden;
    background: var(--backdrop);
  }
  .sheet { position: relative; width: 1200px; height: 900px; }
  .card {
    position: absolute; left: 280px;
    width: 640px; height: 366px;
    overflow: hidden;
    box-shadow: 0 10px 24px rgba(0,0,0,0.35);
  }
  .card--info { top: 60px; }
  .card--brand { top: 474px; }
  .card-shapes { position: absolute; inset: 0; width: 100%; height: 100%; }

  .brand-name {
    position: absolute;
    display: flex; align-items: center; justify-content: center; gap: 12px;
    font-family: "Rajdhani", sans-serif;
    font-weight: 600;
    font-size: 30px;
    line-height: 1.05;
    letter-spacing: 1px;
    text-transform: uppercase;
    color: var(--gold);
    text-align: left;
  }
  .brand-name__mark {
    flex: none;
    width: 22px; height: 22px;
    background: var(--gold);
  }
  .card--info .brand-name { left: 370px; top: 96px; width: 250px; }
  .card--brand .brand-name { left: 170px; top: 140px; width: 300px; }

  .company-line {
    position: absolute; left: 40px; top: 40px;
    font-family: "Orbitron", sans-serif; font-weight: 400;
    font-size: 17px; line-height: 1.35; letter-spacing: 1px;
    color: var(--gold); text-transform: uppercase;
  }
  .company-rule {
    position: absolute; left: 40px; top: 104px;
    width: 180px; height: 3px; background: var(--gold);
  }
  .services {
    position: absolute; left: 40px; top: 120px;
    list-style: none;
    font-family: "Oswald", sans-serif; font-weight: 300;
    font-size: 16px; line-height: 1.5;
    color: var(--text-grey);
  }
  .contact {
    position: absolute; left: 40px; top: 226px;
    font-family: "Oswald", sans-serif; font-weight: 300;
    font-size: 14px; line-height: 1.45;
    color: var(--text-grey);
    font-style: normal;
  }
  .contact__name { color: var(--gold); font-size: 16px; }
  .cityline {
    position: absolute; left: 390px; top: 232px;
    width: 250px; height: 68px;
    background: linear-gradient(180deg, rgba(140,106,5,0) 0%, rgba(140,106,5,0.35) 55%, rgba(86,84,84,0.7) 100%);
  }
  .call {
    position: absolute;
    font-family: "Roboto", sans-serif; font-weight: 400;
    font-size: 19px; letter-spacing: 0.5px;
    color: var(--text-white);
  }
  .card--info .call { right: 26px; top: 308px; }
  .card--brand .call { left: 40px; top: 308px; }
</style>
</head>
<body>
<main class="sheet">

  <section class="card card--info" aria-label="Business card, services side">
    <svg class="card-shapes" viewBox="0 0 640 366" aria-hidden="true">
      <rect width="640" height="366" fill="var(--panel-light)"/>
      <polygon points="0,0 262,0 372,300 372,366 0,366" fill="var(--card-black)"/>
      <polygon points="262,0 326,0 340,172" fill="var(--gold)"/>
      <rect x="240" y="300" width="400" height="40" fill="var(--gold)"/>
      <rect x="200" y="300" width="44" height="40" fill="var(--gold-deep)"/>
      <rect x="0" y="326" width="200" height="40" fill="var(--slate)"/>
      <rect x="200" y="340" width="440" height="26" fill="var(--card-black)"/>
    </svg>
    <p class="company-line">TRV Mechanical<br>Solution</p>
    <div class="company-rule"></div>
    <ul class="services">
      <li>Industrial manufacturing</li>
      <li>construction business</li>
      <li>specializing in consulting project managment</li>
      <li>completing projects turn key</li>
    </ul>
    <address class="contact">
      <span class="contact__name">Gerald Munroe</span><br>
      2847 Alderwick Lane<br>
      Bel Air, MD, 21047
    </address>
    <p class="brand-name"><span class="brand-name__mark"></span><span>TRV Mechanical Solutions</span></p>
    <div class="cityline" role="img" aria-label="Industrial plant skyline with factories and smokestacks"></div>
    <p class="call">CALL: 0305550148</p>
  </section>

  <section class="card card--brand" aria-label="Business card, logo side">
    <svg class="card-shapes" viewBox="0 0 640 366" aria-hidden="true">
      <rect width="640" height="366" fill="var(--card-black)"/>
      <rect x="450" y="262" width="190" height="32" fill="var(--slate)"/>
      <rect x="406" y="282" width="48" height="40" fill="var(--gold-deep)"/>
      <rect x="0" y="300" width="410" height="40" fill="var(--gold)"/>
    </svg>
    <p class="brand-name"><span class="brand-name__mark"></span><span>TRV Mechanical Solutions</span></p>
    <p class="call">CALL: 0305550148</p>
  </section>

</main>
</body>
</html>
```